Brand-new Pediatric Dental Practice needs a website

We are a brand-new dental practice that will specialize in treating children. We want a gorgeous and easily navigable dental practice website that would make a good first impression to potential patients and their parents. It should be modern, SEO-friendly, mobile responsive, and optimized to win new patients.

Target Market(s)

Parents

Industry/Entity Type

Healthcare/Dentistry

Coding

Coded - Design and coding required

Number of Pages Required

4 page

Requirements
Must have
• Use the Wix website building platform. 4 pages: home, meet our dentists, services, contact us
Nice to have
• has a link to our facebook, instagram

```html
<!DOCTYPE html>
<html lang="en">
<head>
<meta charset="utf-8">
<title>Maple Grove – Pediatric Dentistry</title>
<link href="https://fonts.googleapis.com/css2?family=Nunito+Sans:ital,wght@0,300;0,400;0,600;0,700;1,400&display=swap" rel="stylesheet">
<style>
:root{
  --backdrop:#e8e6e5;
  --green:#3a9a5c;
  --green-soft:#e3f1e6;
  --ink:#333336;
  --muted:#8b8b8b;
  --gray-bg:#f6f6f6;
  --line:#c9c9c9;
  --footer:#3a3a3c;
  --wave:#7d917a;
  --white:#ffffff;
}
*{box-sizing:border-box;margin:0;padding:0}
html,body{width:817px;height:1200px;overflow:hidden}
body{background:var(--backdrop);position:relative;font-family:'Nunito Sans',sans-serif;color:var(--ink)}
.page{position:absolute;top:60px;width:455px;background:var(--white);transform:scale(.5165);transform-origin:0 0;overflow:hidden}
.page--home{left:121px;height:2090px}
.page--alt{left:461px;height:1592px}
.block{position:absolute;left:0;width:455px}
a{text-decoration:none;color:inherit}

/* header */
.site-header{top:0;height:50px;z-index:3}
.brand{position:absolute;left:42px;top:14px;display:flex;align-items:center;gap:5px;font-size:13px;font-weight:400;color:var(--ink);letter-spacing:.2px}
.brand-dot{width:13px;height:13px;border-radius:50%;background:var(--green)}
.contact-bar{position:absolute;right:42px;top:8px;display:flex;gap:10px;font-size:6px;align-items:center}
.contact-bar span{display:flex;align-items:center;gap:4px}
.ico{width:14px;height:14px;border-radius:50%;border:1px solid var(--green);display:inline-flex;align-items:center;justify-content:center}
.ico svg{width:7px;height:7px}
.main-nav{position:absolute;right:42px;top:32px;display:flex;gap:12px;font-size:6.5px}
.main-nav .active{color:var(--green)}
.site-header--light .brand,.site-header--light .contact-bar,.site-header--light .main-nav a{color:var(--white)}
.site-header--light .ico{border-color:var(--white)}
.site-header--light .main-nav .active{color:#9fd7a5}

/* hero */
.hero{overflow:hidden}
.hero-photo{position:absolute;inset:0}
.hero--home .hero-photo{background:
  radial-gradient(ellipse 120px 130px at 345px 130px,#f3dcc6 0%,#e4bf9c 40%,rgba(196,150,98,.6) 70%,rgba(150,120,70,0) 100%),
  radial-gradient(ellipse 150px 170px at 360px 80px,#a7794a 0%,rgba(130,100,60,.6) 60%,rgba(120,120,60,0) 100%),
  linear-gradient(100deg,#1e5627 0%,#2b6f2d 30%,#5a8c3a 52%,#9a9a5e 72%,#b9a58a 100%)}
.hero--alt .hero-photo{background:
  radial-gradient(ellipse 110px 120px at 345px 120px,#f4d5b8 0%,#e6b38a 45%,rgba(214,140,80,0) 100%),
  radial-gradient(ellipse 80px 110px at 200px 80px,rgba(220,170,130,.85) 0%,rgba(200,150,110,0) 100%),
  linear-gradient(100deg,#2a6a2a 0%,#4a8e34 30%,#8aa858 50%,#c79d74 70%,#6e9a4c 100%)}
.hero h1{position:absolute;left:42px;font-size:20px;font-weight:400;color:var(--white)}
.hero p{position:absolute;left:43px;width:190px;font-size:7px;line-height:12px;color:var(--white)}
.btn-outline{display:inline-block;border:1px solid var(--green);color:var(--green);border-radius:12px;font-size:5.8px;font-weight:700;padding:6px 8px;letter-spacing:.3px}
.hero .btn-light{position:absolute;left:42px;border:1px solid var(--white);color:var(--white);border-radius:12px;font-size:5.8px;font-weight:700;padding:7px 10px}
.hero-wave{position:absolute;left:0;bottom:-1px;width:455px;height:90px}

/* welcome */
.welcome .emblem{position:absolute;left:42px;width:158px;height:145px;border-radius:50%;background:radial-gradient(circle,#f8f8f8 0%,#f1f1f1 100%);display:flex;align-items:center;justify-content:center;text-align:center;color:var(--green);font-weight:700;font-size:15px;line-height:21px}
.welcome h2{position:absolute;left:234px;font-size:15px;font-weight:400}
.welcome p{position:absolute;left:234px;width:186px;font-size:5.4px;line-height:10.6px;color:var(--muted)}
.welcome .btn-outline{position:absolute;left:234px}

/* services */
.services{background:var(--gray-bg)}
.section-title{position:absolute;left:0;width:455px;text-align:center;font-size:15px;font-weight:400}
.service-grid{position:absolute;left:42px;width:371px;display:grid;grid-template-columns:repeat(3,118px);column-gap:8.5px}
.service{position:relative;height:206px;text-align:center}
.service .photo{height:94px}
.service-icon{position:absolute;left:47px;top:76px;width:24px;height:24px;border-radius:50%;background:var(--white);display:flex;align-items:center;justify-content:center}
.service-icon svg{width:14px;height:14px}
.service h3{margin-top:26px;font-size:8px;font-weight:400}
.service p{margin-top:5px;font-size:5px;line-height:9.5px;color:var(--muted)}
.service .btn-outline{margin-top:7px}

/* photo fills */
.ph-a{background:radial-gradient(ellipse 40px 45px at 40% 55%,#f0d4bb 0%,rgba(220,180,140,0) 100%),radial-gradient(ellipse 35px 40px at 78% 60%,#d9ae88 0%,rgba(200,160,120,0) 100%),linear-gradient(180deg,#4f8a3a 0%,#7fa255 50%,#d8d2c8 100%)}
.ph-b{background:radial-gradient(ellipse 45px 50px at 75% 45%,#ecc9ae 0%,rgba(220,180,150,0) 100%),linear-gradient(135deg,#a98a72 0%,#c8a58c 50%,#d9bfaa 100%)}
.ph-c{background:radial-gradient(ellipse 35px 42px at 50% 45%,#f0cdb2 0%,rgba(230,190,160,0) 100%),radial-gradient(ellipse 30px 20px at 50% 95%,#a9c44a 0%,rgba(170,196,74,0) 100%),linear-gradient(180deg,#dcdde0 0%,#cfcfd4 100%)}
.ph-d{background:radial-gradient(ellipse 40px 40px at 55% 45%,#c99c7d 0%,rgba(190,150,120,0) 100%),radial-gradient(ellipse 30px 25px at 90% 80%,#9fcf5a 0%,rgba(160,200,90,0) 100%),linear-gradient(135deg,#6d7a83 0%,#9aa4ab 50%,#c9d2d6 100%)}
.ph-e{background:radial-gradient(ellipse 25px 40px at 50% 50%,#e7c2a4 0%,rgba(230,190,160,0) 100%),linear-gradient(135deg,#78bd48 0%,#88c458 100%)}
.ph-f{background:radial-gradient(ellipse 35px 35px at 30% 35%,#e8c4a6 0%,rgba(230,190,160,0) 100%),radial-gradient(ellipse 30px 35px at 75% 65%,#f0d2b8 0%,rgba(230,200,170,0) 100%),linear-gradient(135deg,#9dc27a 0%,#d6cfc6 45%,#b7c7d0 100%)}
.ph-doc{background:radial-gradient(ellipse 20px 24px at 50% 30%,#ecc7a8 0%,rgba(230,190,160,0) 100%),radial-gradient(ellipse 50px 40px at 50% 100%,#e9eef2 0%,rgba(230,236,240,0) 100%),linear-gradient(180deg,#ffffff 0%,#f4f4f4 100%)}

/* why choose */
.why h2{position:absolute;left:42px;top:28px;font-size:15px;font-weight:400;line-height:21px}
.why .lead{position:absolute;left:42px;top:80px;width:150px;font-size:5.4px;line-height:10px;color:var(--muted)}
.why-list{position:absolute;left:42px;top:110px;list-style:none}
.why-list li{display:flex;align-items:center;gap:8px;height:28px;font-size:6px;font-weight:600}
.why-dot{width:19px;height:19px;border-radius:50%;background:var(--green-soft);display:flex;align-items:center;justify-content:center}
.why-dot svg{width:9px;height:9px}
.why .btn-outline{position:absolute;left:42px;top:200px}
.video{position:absolute;left:204px;top:32px;width:209px;height:141px;background:radial-gradient(ellipse 45px 45px at 68% 45%,#efccb0 0%,rgba(230,190,160,0) 100%),radial-gradient(ellipse 60px 30px at 55% 100%,#9fce63 0%,rgba(160,206,99,0) 100%),linear-gradient(120deg,#5e6c7c 0%,#dfe4ea 30%,#f1f1f1 60%,#dcdcdc 100%)}
.play{position:absolute;left:92px;top:58px;width:24px;height:24px;border-radius:50%;background:rgba(30,30,30,.75);display:flex;align-items:center;justify-content:center}

/* testimonial */
.testimonial .photo{position:absolute;inset:0;background:radial-gradient(ellipse 70px 60px at 80px 110px,#efd1b8 0%,rgba(230,190,160,0) 100%),radial-gradient(ellipse 110px 70px at 110px 200px,#9fd36a 0%,rgba(150,200,100,0) 100%),linear-gradient(110deg,#c6a38a 0%,#e8dcd2 30%,#cfe6c0 50%,#dcdddf 75%,#8c8f93 100%)}
.quote-card{position:absolute;left:238px;top:24px;width:172px;height:172px;border-radius:50%;background:rgba(255,255,255,.8);text-align:center}
.quote-mark{position:absolute;left:0;width:172px;top:22px;font-size:30px;font-weight:700;color:var(--green);line-height:1}
.quote-card blockquote{position:absolute;left:8px;top:60px;width:156px;font-style:italic;font-size:8.4px;line-height:12.5px}
.quote-card cite{position:absolute;left:0;top:118px;width:172px;font-style:normal;font-size:7px}
.dots{position:absolute;left:78px;top:143px;display:flex;gap:2px}
.dots i{width:4px;height:4px;border-radius:50%;border:.7px solid var(--muted)}
.dots i:first-child{background:var(--muted)}

/* dentists */
.dentists{background:var(--green)}
.dentists .section-title{color:var(--white)}
.dentist-grid{position:absolute;left:42px;width:371px;display:grid;grid-template-columns:repeat(4,87px);column-gap:7.3px;text-align:center;color:var(--white)}
.dentist .photo{height:97px}
.dentist h3{margin-top:7px;font-size:7px;font-weight:700}
.dentist span{display:block;font-size:5.4px;line-height:9px}
.arrow{position:absolute;width:10px;height:10px}

/* contact */
.contact-form{position:absolute;left:76px;width:314px;display:grid;grid-template-columns:154px 154px;column-gap:6px}
.fields{display:flex;flex-direction:column;gap:5px}
.field{height:20px;border:1px solid var(--line);font-size:5.5px;color:var(--muted);padding:5px 6px}
.field--message{height:70px}
.btn-solid{position:absolute;left:204px;width:47px;height:20px;border-radius:10px;background:var(--green);color:var(--white);font-size:6px;font-weight:700;display:flex;align-items:center;justify-content:center}

/* footer */
.site-footer svg.footer-wave{position:absolute;left:0;top:0;width:455px}
.footer-brand{position:absolute;left:42px;display:flex;align-items:center;gap:6px;font-size:17px;color:var(--white)}
.footer-brand .brand-dot{width:20px;height:20px}
.footer-col{position:absolute;font-size:5.6px;line-height:11px;color:#d6d6d6}
.footer-col h4{font-size:6px;font-weight:700;color:var(--white);margin-bottom:6px}
.footer-col .g{color:var(--green)}
.footer-rule{position:absolute;left:42px;width:371px;height:1px;background:#5a5a5c}
.copyright{position:absolute;left:42px;font-size:5.6px;color:#cfcfcf}
.social{position:absolute;right:42px;display:flex;gap:5px}
.social i{width:15px;height:15px;border-radius:50%;border:1px solid var(--green)}
</style>
</head>
<body>

<!-- ================= Home page ================= -->
<div class="page page--home">

  <header class="block site-header">
    <div class="brand"><span class="brand-dot"></span>maple grove</div>
    <div class="contact-bar">
      <span><i class="ico"><svg viewBox="0 0 10 10"><path d="M2 1l2 2-1 1.3c.6 1.2 1.5 2.1 2.7 2.7L7 6l2 2-1.3 1.5C4.5 9.2.8 5.5.5 2.3z" fill="#3a9a5c"/></svg></i>1 555 010 2040</span>
      <span><i class="ico"><svg viewBox="0 0 10 10"><rect x="1" y="2.5" width="8" height="5.5" fill="#3a9a5c"/><path d="M1 2.5l4 3 4-3" stroke="#fff" stroke-width=".8" fill="none"/></svg></i>hello@maplegrove.example</span>
    </div>
    <nav class="main-nav"><a class="active">Home</a><a>Meet our dentists</a><a>Services</a><a>Contact us</a></nav>
  </header>

  <section class="block hero hero--home" style="top:50px;height:272px">
    <div class="hero-photo" role="img" aria-label="Smiling young girl on a green garden background"></div>
    <h1 style="top:60px">Pediatric Dentistry</h1>
    <p style="top:92px">We are a brand-new dental practice that will specialize in treating children.</p>
    <a class="btn-light" style="top:130px">MAKE AN APPOINMENT</a>
    <svg class="hero-wave" viewBox="0 0 455 90" preserveAspectRatio="none">
      <path d="M0 46 C30 20 70 2 120 12 C170 22 205 80 255 86 C320 92 370 30 420 22 C440 20 450 30 455 38 L455 90 L0 90Z" fill="#fff"/>
      <path d="M0 44 C30 18 70 0 120 10 C170 20 205 78 255 84 C320 90 370 28 420 20 C440 18 450 28 455 36" fill="none" stroke="#7d917a" stroke-width="3"/>
    </svg>
  </section>

  <section class="block welcome" style="top:322px;height:181px">
    <div class="emblem" style="top:8px">Pediatric<br>Dental<br>Practice</div>
    <h2 style="top:24px">Welcome to Maple Grove</h2>
    <p style="top:50px">Nemo enim ipsam voluptatem quia voluptas sit aspernatur aut odit aut fugit, sed quia consequuntur magni doloreeos qui ratione voluptatem sequi nesciunt. Neque porro quisqu am est, qui dolorem ipsum non numquam eius modi temp ora incidunt ut labore et dolore.</p>
    <a class="btn-outline" style="top:116px">READ MORE</a>
  </section>

  <section class="block services" style="top:503px;height:485px">
    <h2 class="section-title" style="top:24px">Our Services</h2>
    <div class="service-grid" style="top:57px">
      <div class="service"><div class="photo ph-a" role="img" aria-label="Two smiling sisters outdoors"></div><span class="service-icon"><svg viewBox="0 0 14 14"><rect x="2" y="5" width="10" height="4" rx="2" fill="none" stroke="#3a9a5c"/><path d="M4.5 5v4M7 5v4M9.5 5v4" stroke="#3a9a5c" stroke-width=".8"/></svg></span><h3>Early Orthodontics</h3><p>Excepteur sint occaecat cupidatat non proident, sunt in culpa qui offi cia deserunt mollit anim id.</p><a class="btn-outline">READ MORE</a></div>
      <div class="service"><div class="photo ph-b" role="img" aria-label="Baby having gums cleaned with a finger brush"></div><span class="service-icon"><svg viewBox="0 0 14 14"><circle cx="7" cy="7.5" r="5" fill="none" stroke="#3a9a5c"/><path d="M4.5 8.5c1.5 1.6 3.5 1.6 5 0" fill="none" stroke="#3a9a5c" stroke-width=".8"/></svg></span><h3>Infant Oral Care</h3><p>Excepteur sint occaecat cupidatat non proident, sunt in culpa qui offi cia deserunt mollit anim id.</p><a class="btn-outline">READ MORE</a></div>
      <div class="service"><div class="photo ph-c" role="img" aria-label="Toddler brushing her teeth"></div><span class="service-icon"><svg viewBox="0 0 14 14"><path d="M3 3c2-1 3 0 4 0s2-1 4 0c1 2 0 4-1 5l-1 4-1.5-3h-1L5 12 4 8C3 7 2 5 3 3z" fill="none" stroke="#3a9a5c"/></svg></span><h3>Preventive Dentistry</h3><p>Excepteur sint occaecat cupidatat non proident, sunt in culpa qui offi cia deserunt mollit anim id.</p><a class="btn-outline">READ MORE</a></div>
      <div class="service"><div class="photo ph-d" role="img" aria-label="Boy relaxing with a nasal sedation mask"></div><span class="service-icon"><svg viewBox="0 0 14 14"><path d="M3 3c2-1 3 0 4 0s2-1 4 0c1 2 0 4-1 5l-1 4-1.5-3h-1L5 12 4 8C3 7 2 5 3 3z" fill="none" stroke="#3a9a5c"/></svg></span><h3>Sedation Dentistry</h3><p>Excepteur sint occaecat cupidatat non proident, sunt in culpa qui offi cia deserunt mollit anim id.</p><a class="btn-outline">READ MORE</a></div>
      <div class="service"><div class="photo ph-e" role="img" aria-label="Girl holding her cheek on a green background"></div><span class="service-icon"><svg viewBox="0 0 14 14"><path d="M3 3c2-1 3 0 4 0s2-1 4 0c1 2 0 4-1 5l-1 4-1.5-3h-1L5 12 4 8C3 7 2 5 3 3z" fill="none" stroke="#3a9a5c"/></svg></span><h3>Emergency Care</h3><p>Excepteur sint occaecat cupidatat non proident, sunt in culpa qui offi cia deserunt mollit anim id.</p><a class="btn-outline">READ MORE</a></div>
      <div class="service"><div class="photo ph-f" role="img" aria-label="Dentist smiling with a young patient"></div><span class="service-icon"><svg viewBox="0 0 14 14"><circle cx="7" cy="7" r="5" fill="none" stroke="#3a9a5c"/><path d="M5 7l1.5 1.5L9.5 5.5" fill="none" stroke="#3a9a5c"/></svg></span><h3>Pediatric Dentistry</h3><p>Excepteur sint occaecat cupidatat non proident, sunt in culpa qui offi cia deserunt mollit anim id.</p><a class="btn-outline">READ MORE</a></div>
    </div>
  </section>

  <section class="block why" style="top:988px;height:250px">
    <h2>Why Choose<br>Maple Grove</h2>
    <p class="lead">Nemo enim ipsam voluptatem quia voluptas sit aspernatur aut odit aut fugit.</p>
    <ul class="why-list">
      <li><span class="why-dot"><svg viewBox="0 0 10 10"><circle cx="5" cy="5" r="4" fill="none" stroke="#3a9a5c"/><path d="M3 6c1 1 3 1 4 0" fill="none" stroke="#3a9a5c" stroke-width=".8"/></svg></span>Fun &amp; Engaging</li>
      <li><span class="why-dot"><svg viewBox="0 0 10 10"><circle cx="5" cy="3.5" r="2" fill="#3a9a5c"/><path d="M1.5 9c.5-2.5 6.5-2.5 7 0z" fill="#3a9a5c"/></svg></span>Specialized Team</li>
      <li><span class="why-dot"><svg viewBox="0 0 10 10"><circle cx="5" cy="5" r="4" fill="none" stroke="#3a9a5c"/><path d="M5 2.5V5l1.8 1.2" fill="none" stroke="#3a9a5c" stroke-width=".8"/></svg></span>Convenient appointment options</li>
    </ul>
    <a class="btn-outline">READ MORE</a>
    <div class="video" role="img" aria-label="Video still of a dentist examining a smiling girl">
      <span class="play"><svg width="8" height="9" viewBox="0 0 8 9"><path d="M1 0l7 4.5L1 9z" fill="#fff"/></svg></span>
    </div>
  </section>

  <section class="block testimonial" style="top:1238px;height:220px">
    <div class="photo" role="img" aria-label="Girl in a green dental chair during a check-up"></div>
    <div class="quote-card">
      <span class="quote-mark">&#8220;</span>
      <blockquote>“ Nemo enim ipsam volupta tem quia voluptas sit aspernat ur aut odit aut fugit, sed quia conlu sequuntu ”</blockquote>
      <cite>- Dana K</cite>
      <span class="dots"><i></i><i></i><i></i></span>
    </div>
  </section>

  <section class="block dentists" style="top:1458px;height:212px">
    <h2 class="section-title" style="top:24px">Meet Our Dentists</h2>
    <svg class="arrow" style="left:21px;top:102px" viewBox="0 0 10 10"><path d="M6.5 2L3.5 5l3 3" fill="none" stroke="#fff"/></svg>
    <svg class="arrow" style="left:424px;top:102px" viewBox="0 0 10 10"><path d="M3.5 2l3 3-3 3" fill="none" stroke="#fff"/></svg>
    <div class="dentist-grid" style="top:59px">
      <div class="dentist"><div class="photo ph-doc" role="img" aria-label="Portrait of Dr. Nora in a white coat"></div><h3>Dr. Nora</h3><span>Voluptatem acc</span></div>
      <div class="dentist"><div class="photo ph-doc" role="img" aria-label="Portrait of Dr. Sam Reed in a white coat"></div><h3>Dr. Sam Reed</h3><span>Voluptatem acc</span></div>
      <div class="dentist"><div class="photo ph-doc" role="img" aria-label="Portrait of Dr. Ava in a white coat"></div><h3>Dr. Ava</h3><span>Voluptatem acc</span></div>
      <div class="dentist"><div class="photo ph-doc" role="img" aria-label="Portrait of Dr. Leo in a white coat"></div><h3>Dr. Leo</h3><span>Voluptatem acc</span></div>
    </div>
  </section>

  <section class="block contact" style="top:1670px;height:170px">
    <h2 class="section-title" style="top:24px">Contact Us</h2>
    <div class="contact-form" style="top:59px">
      <div class="fields"><div class="field">Name</div><div class="field">Email</div><div class="field">Phone Number</div></div>
      <div class="field field--message">Message</div>
    </div>
    <a class="btn-solid" style="top:147px">SUBMIT</a>
  </section>

  <footer class="block site-footer" style="top:1850px;height:240px">
    <svg class="footer-wave" height="240" viewBox="0 0 455 240" preserveAspectRatio="none">
      <path d="M0 44 C30 70 70 72 110 50 C160 20 200 6 245 22 C290 40 320 72 370 70 C410 68 440 50 455 40 L455 240 L0 240Z" fill="#3a3a3c"/>
      <path d="M0 40 C30 66 70 68 110 46 C160 16 200 2 245 18 C290 36 320 68 370 66 C410 64 440 46 455 36" fill="none" stroke="#7d917a" stroke-width="4"/>
    </svg>
    <div class="footer-brand" style="top:125px"><span class="brand-dot"></span>maple grove</div>
    <div class="footer-col" style="left:181px;top:111px"><h4>Quick Links</h4>Home<br>Meet our dentists<br>Services<br>Contact us</div>
    <div class="footer-col" style="left:273px;top:111px"><h4>Contact Us</h4><span class="g">&#9679;</span> 220 Birch Lane, Suite 12,<br>&nbsp;&nbsp;&nbsp;Fairview, 482910<br><span class="g">&#9679;</span> 1 555 010 2040<br><br><span class="g">&#9679;</span> hello@maplegrove.example</div>
    <div class="footer-rule" style="top:204px"></div>
    <div class="copyright" style="top:215px">Copyright © 2022, Maple Grove. All rights reserved.</div>
    <div class="social" style="top:211px"><i></i><i></i></div>
  </footer>
</div>

<!-- ================= Alternate home page ================= -->
<div class="page page--alt">

  <section class="block hero hero--alt" style="top:0;height:290px">
    <div class="hero-photo" role="img" aria-label="Two smiling young sisters close up"></div>
    <h1 style="top:92px">Pediatric Dentistry</h1>
    <p style="top:125px">We are a brand-new dental practice that will specialize in treating children.</p>
    <a class="btn-light" style="top:165px">MAKE AN APPOINMENT</a>
    <svg class="hero-wave" viewBox="0 0 455 90" preserveAspectRatio="none">
      <path d="M0 80 C20 40 50 20 100 26 C160 34 200 70 260 66 C320 62 360 20 410 22 C435 24 450 40 455 48 L455 90 L0 90Z" fill="#fff"/>
      <path d="M0 78 C20 38 50 18 100 24 C160 32 200 68 260 64 C320 60 360 18 410 20 C435 22 450 38 455 46" fill="none" stroke="#7d917a" stroke-width="3"/>
    </svg>
  </section>

  <header class="block site-header site-header--light">
    <div class="brand"><span class="brand-dot"></span>maple grove</div>
    <div class="contact-bar">
      <span><i class="ico"><svg viewBox="0 0 10 10"><path d="M2 1l2 2-1 1.3c.6 1.2 1.5 2.1 2.7 2.7L7 6l2 2-1.3 1.5C4.5 9.2.8 5.5.5 2.3z" fill="#fff"/></svg></i>1 555 010 2040</span>
      <span><i class="ico"><svg viewBox="0 0 10 10"><rect x="1" y="2.5" width="8" height="5.5" fill="#fff"/></svg></i>hello@maplegrove.example</span>
    </div>
    <nav class="main-nav"><a class="active">Home</a><a>Meet our dentists</a><a>Services</a><a>Contact us</a></nav>
  </header>

  <section class="block welcome" style="top:290px;height:193px">
    <div class="emblem" style="top:20px">Pediatric<br>Dental<br>Practice</div>
    <h2 style="top:36px">Welcome to Maple Grove</h2>
    <p style="top:62px">Nemo enim ipsam voluptatem quia voluptas sit aspernatur aut odit aut fugit, sed quia consequuntur magni doloreeos qui ratione voluptatem sequi nesciunt. Neque porro quisqu am est, qui dolorem ipsum non numquam eius modi temp ora incidunt ut labore et dolore.</p>
    <a class="btn-outline" style="top:128px">READ MORE</a>
  </section>

  <section class="block services" style="top:483px;height:482px">
    <h2 class="section-title" style="top:24px">Our Services</h2>
    <div class="service-grid" style="top:57px">
      <div class="service"><div class="photo ph-a" role="img" aria-label="Two smiling sisters outdoors"></div><span class="service-icon"><svg viewBox="0 0 14 14"><rect x="2" y="5" width="10" height="4" rx="2" fill="none" stroke="#3a9a5c"/><path d="M4.5 5v4M7 5v4M9.5 5v4" stroke="#3a9a5c" stroke-width=".8"/></svg></span><h3>Early Orthodontics</h3><p>Excepteur sint occaecat cupidatat non proident, sunt in culpa qui offi cia deserunt mollit anim id.</p><a class="btn-outline">READ MORE</a></div>
      <div class="service"><div class="photo ph-b" role="img" aria-label="Baby having gums cleaned with a finger brush"></div><span class="service-icon"><svg viewBox="0 0 14 14"><circle cx="7" cy="7.5" r="5" fill="none" stroke="#3a9a5c"/><path d="M4.5 8.5c1.5 1.6 3.5 1.6 5 0" fill="none" stroke="#3a9a5c" stroke-width=".8"/></svg></span><h3>Infant Oral Care</h3><p>Excepteur sint occaecat cupidatat non proident, sunt in culpa qui offi cia deserunt mollit anim id.</p><a class="btn-outline">READ MORE</a></div>
      <div class="service"><div class="photo ph-c" role="img" aria-label="Toddler brushing her teeth"></div><span class="service-icon"><svg viewBox="0 0 14 14"><path d="M3 3c2-1 3 0 4 0s2-1 4 0c1 2 0 4-1 5l-1 4-1.5-3h-1L5 12 4 8C3 7 2 5 3 3z" fill="none" stroke="#3a9a5c"/></svg></span><h3>Preventive Dentistry</h3><p>Excepteur sint occaecat cupidatat non proident, sunt in culpa qui offi cia deserunt mollit anim id.</p><a class="btn-outline">READ MORE</a></div>
      <div class="service"><div class="photo ph-d" role="img" aria-label="Boy relaxing with a nasal sedation mask"></div><span class="service-icon"><svg viewBox="0 0 14 14"><path d="M3 3c2-1 3 0 4 0s2-1 4 0c1 2 0 4-1 5l-1 4-1.5-3h-1L5 12 4 8C3 7 2 5 3 3z" fill="none" stroke="#3a9a5c"/></svg></span><h3>Sedation Dentistry</h3><p>Excepteur sint occaecat cupidatat non proident, sunt in culpa qui offi cia deserunt mollit anim id.</p><a class="btn-outline">READ MORE</a></div>
      <div class="service"><div class="photo ph-e" role="img" aria-label="Girl holding her cheek on a green background"></div><span class="service-icon"><svg viewBox="0 0 14 14"><path d="M3 3c2-1 3 0 4 0s2-1 4 0c1 2 0 4-1 5l-1 4-1.5-3h-1L5 12 4 8C3 7 2 5 3 3z" fill="none" stroke="#3a9a5c"/></svg></span><h3>Emergency Care</h3><p>Excepteur sint occaecat cupidatat non proident, sunt in culpa qui offi cia deserunt mollit anim id.</p><a class="btn-outline">READ MORE</a></div>
      <div class="service"><div class="photo ph-f" role="img" aria-label="Dentist smiling with a young patient"></div><span class="service-icon"><svg viewBox="0 0 14 14"><circle cx="7" cy="7" r="5" fill="none" stroke="#3a9a5c"/><path d="M5 7l1.5 1.5L9.5 5.5" fill="none" stroke="#3a9a5c"/></svg></span><h3>Pediatric Dentistry</h3><p>Excepteur sint occaecat cupidatat non proident, sunt in culpa qui offi cia deserunt mollit anim id.</p><a class="btn-outline">READ MORE</a></div>
    </div>
  </section>

  <section class="block dentists" style="top:965px;height:212px">
    <h2 class="section-title" style="top:24px">Meet Our Dentists</h2>
    <svg class="arrow" style="left:21px;top:102px" viewBox="0 0 10 10"><path d="M6.5 2L3.5 5l3 3" fill="none" stroke="#fff"/></svg>
    <svg class="arrow" style="left:424px;top:102px" viewBox="0 0 10 10"><path d="M3.5 2l3 3-3 3" fill="none" stroke="#fff"/></svg>
    <div class="dentist-grid" style="top:58px">
      <div class="dentist"><div class="photo ph-doc" role="img" aria-label="Portrait of Dr. Nora in a white coat"></div><h3>Dr. Nora</h3><span>Voluptatem acc</span></div>
      <div class="dentist"><div class="photo ph-doc" role="img" aria-label="Portrait of Dr. Sam Reed in a white coat"></div><h3>Dr. Sam Reed</h3><span>Voluptatem acc</span></div>
      <div class="dentist"><div class="photo ph-doc" role="img" aria-label="Portrait of Dr. Ava in a white coat"></div><h3>Dr. Ava</h3><span>Voluptatem acc</span></div>
      <div class="dentist"><div class="photo ph-doc" role="img" aria-label="Portrait of Dr. Leo in a white coat"></div><h3>Dr. Leo</h3><span>Voluptatem acc</span></div>
    </div>
  </section>

  <section class="block contact" style="top:1177px;height:180px">
    <h2 class="section-title" style="top:24px">Contact Us</h2>
    <div class="contact-form" style="top:58px">
      <div class="fields"><div class="field">Name</div><div class="field">Email</div><div class="field">Phone Number</div></div>
      <div class="field field--message">Message</div>
    </div>
    <a class="btn-solid" style="top:146px">SUBMIT</a>
  </section>

  <footer class="block site-footer" style="top:1360px;height:232px">
    <svg class="footer-wave" height="232" viewBox="0 0 455 232" preserveAspectRatio="none">
      <path d="M0 36 C30 66 70 70 110 48 C160 18 200 4 245 20 C290 38 320 70 370 68 C410 66 440 48 455 38 L455 232 L0 232Z" fill="#3a3a3c"/>
      <path d="M0 32 C30 62 70 66 110 44 C160 14 200 0 245 16 C290 34 320 66 370 64 C410 62 440 44 455 34" fill="none" stroke="#7d917a" stroke-width="4"/>
    </svg>
    <div class="footer-brand" style="top:118px"><span class="brand-dot"></span>maple grove</div>
    <div class="footer-col" style="left:181px;top:103px"><h4>Quick Links</h4>Home<br>Meet our dentists<br>Services<br>Contact us</div>
    <div class="footer-col" style="left:273px;top:103px"><h4>Contact Us</h4><span class="g">&#9679;</span> 220 Birch Lane, Suite 12,<br>&nbsp;&nbsp;&nbsp;Fairview, 482910<br><span class="g">&#9679;</span> 1 555 010 2040<br><br><span class="g">&#9679;</span> hello@maplegrove.example</div>
    <div class="footer-rule" style="top:196px"></div>
    <div class="copyright" style="top:208px">Copyright © 2022, Maple Grove. All rights reserved.</div>
    <div class="social" style="top:204px"><i></i><i></i></div>
  </footer>
</div>

</body>
</html>
```